Harbor Compass - Book Cover

I need a book cover for my debut work, "Harbor Compass - Turning the Tide, One Step at a Time." While the website isn't complete, you can get a sense of what I am writing about by looking at my website, harborcompassbooks.org. The book is a leadership development book, but more of a personal change journey. The emphasis is on figuring out how to combine you work, social, and own self into an authentic package that not only resonates with others, but makes what you achieve more fulfilling.

I am attaching a copy of my logo so you can get a sense of what I like. I would prefer to not have the cover be photographic, but am open to suggestions. This will be a series of books so maintaining some sense of style will be important, and can garner future work.

Industry/Entity Type

Leadership

```html
<!DOCTYPE html>
<html lang="en">
<head>
<meta charset="utf-8">
<title>Harbor Compass – Book Cover</title>
<link href="https://fonts.googleapis.com/css2?family=Cinzel:wght@500&family=Montserrat:wght@400;500&display=swap" rel="stylesheet">
<style>
  :root {
    --sky-top: #18191d;
    --cloud-band: #5b5650;
    --sky-mid: #3a5478;
    --sky-glow: #c6d0da;
    --ridge: #2b2d31;
    --ground: #1c1d20;
    --brand-blue: #2a9fe0;
    --accent-orange: #e46a2e;
    --title-white: #ffffff;
    --author-blue: #27aee6;
  }
  html, body {
    margin: 0;
    padding: 0;
    overflow: hidden;
    background: #111;
  }
  .cover {
    position: relative;
    width: 800px;
    height: 1200px;
    overflow: hidden;
  }
  .cover-scene {
    position: absolute;
    inset: 0;
    background: linear-gradient(
      to bottom,
      var(--sky-top) 0%,
      #25262a 18%,
      var(--cloud-band) 27%,
      #36404d 36%,
      var(--sky-mid) 48%,
      #6f87a2 56%,
      var(--sky-glow) 61%,
      #8a9bb0 67%,
      var(--ridge) 74%,
      var(--ground) 100%
    );
  }
  .brand {
    position: absolute;
    top: 70px;
    left: 88px;
    display: flex;
    align-items: center;
    gap: 16px;
  }
  .brand-dot {
    width: 132px;
    height: 132px;
    border-radius: 50%;
    background: var(--brand-blue);
  }
  .brand-name {
    font-family: "Montserrat", sans-serif;
    font-weight: 500;
    font-size: 52px;
    color: var(--brand-blue);
    margin-top: 40px;
  }
  .tagline {
    position: absolute;
    left: 0;
    width: 800px;
    text-align: center;
    margin: 0;
  }
  .tagline-lead {
    top: 198px;
    font-family: "Cinzel", serif;
    font-weight: 500;
    font-size: 27px;
    color: var(--accent-orange);
    padding-left: 40px;
  }
  .tagline-main {
    top: 240px;
    font-family: "Montserrat", sans-serif;
    font-weight: 400;
    font-size: 42px;
    letter-spacing: 2px;
    color: var(--title-white);
  }
  .author {
    position: absolute;
    top: 1092px;
    left: 0;
    width: 800px;
    text-align: center;
    margin: 0;
    font-family: "Montserrat", sans-serif;
    font-weight: 400;
    font-size: 36px;
    letter-spacing: 7px;
    color: var(--author-blue);
  }
</style>
</head>
<body>
  <main class="cover">
    <div class="cover-scene" role="img" aria-label="Photograph of a dramatic cloudy sky over snowy mountains, with a person standing arms outstretched on a rock summit"></div>

    <div class="brand">
      <span class="brand-dot"></span>
      <span class="brand-name">Harbor Compass</span>
    </div>

    <p class="tagline tagline-lead">TURNING THE TIDE,</p>
    <h1 class="tagline tagline-main">ONE STEP AT A TIME</h1>

    <p class="author">DANIEL HALE</p>
  </main>
</body>
</html>
```